BrivoLane Ute.

I want the full logo on one side. And the other side the card if right Ralf the logo the left half orange like the car in the logo color with Danielle R Morrow
Founder and CEO
Email symbol then dmorrow@brivolaneute.com
Www symbol. Then Brivolaneute.com
Phone symbol then 413-926-BRIV
The very bottom would like Brivo Lane Ute is a division of Harmond Vistas. LLC

```html
<!DOCTYPE html>
<html lang="en">
<head>
<meta charset="utf-8">
<title>BrivoLane Ute — Business Card</title>
<link rel="stylesheet" href="https://fonts.googleapis.com/css2?family=Arimo:wght@400;700&display=swap">
<style>
  :root {
    --bg: #2b2b2d;
    --white: #ffffff;
    --orange: #ec8e26;
    --orange-light: #f6a948;
    --red: #e6332e;
    --peach: #f8c7a2;
    --ink: #1d1d1d;
    --teal: #8fd3c6;
  }
  * { margin: 0; padding: 0; box-sizing: border-box; }
  html, body { width: 1200px; height: 912px; overflow: hidden; }
  body {
    background: var(--bg);
    font-family: "Arimo", Arial, sans-serif;
    display: flex;
    flex-direction: column;
    align-items: center;
    justify-content: center;
    gap: 56px;
  }
  .card {
    position: relative;
    width: 620px;
    height: 354px;
    border-radius: 22px;
    overflow: hidden;
    background: var(--white);
    box-shadow: 0 10px 24px rgba(0,0,0,.45);
  }
  .card svg.swoosh { position: absolute; inset: 0; }
  .logo {
    position: absolute;
    display: flex;
    flex-direction: column;
    align-items: center;
    gap: 10px;
  }
  .logo-art {
    width: 230px;
    height: 96px;
    border-radius: 10px;
    background: linear-gradient(180deg, var(--teal) 0%, var(--orange) 55%, #b86a1c 100%);
  }
  .logo-name {
    font-weight: 700;
    font-size: 34px;
    color: var(--ink);
    letter-spacing: 1px;
    white-space: nowrap;
  }
  .card--front .logo { left: 150px; top: 34px; }
  .front-url {
    position: absolute;
    left: 325px;
    top: 172px;
    color: var(--orange);
    font-size: 14px;
    letter-spacing: 1.5px;
    white-space: nowrap;
    transform: rotate(-25deg);
    transform-origin: center;
  }
  .card--back { background: var(--orange); }
  .card--back .logo { left: 345px; top: 46px; transform: scale(.88); transform-origin: top left; }
  .identity { position: absolute; left: 32px; top: 40px; color: var(--white); }
  .identity .name { font-size: 20px; font-weight: 400; letter-spacing: 1px; text-transform: uppercase; }
  .identity .role { font-size: 14px; letter-spacing: 1px; text-transform: uppercase; margin-top: 3px; }
  .contacts { position: absolute; left: 32px; top: 214px; list-style: none; color: var(--white); font-size: 17px; }
  .contacts li { display: flex; align-items: center; gap: 12px; height: 30px; }
  .contacts svg { width: 18px; height: 18px; flex: none; }
  .division { position: absolute; left: 32px; bottom: 20px; color: var(--white); font-size: 13px; }
</style>
</head>
<body>

  <section class="card card--front" aria-label="Card front">
    <svg class="swoosh" viewBox="0 0 620 354" width="620" height="354" aria-hidden="true">
      <path d="M0,290 C210,292 460,240 620,70 L620,354 L0,354 Z" fill="var(--peach)"/>
      <path d="M0,303 C215,305 465,255 620,92 L620,354 L0,354 Z" fill="var(--red)"/>
      <path d="M0,318 C222,320 472,272 620,118 L620,354 L0,354 Z" fill="var(--orange)"/>
    </svg>
    <div class="logo">
      <div class="logo-art" role="img" aria-label="Brand illustration area"></div>
      <div class="logo-name">BrivoLane Ute</div>
    </div>
    <div class="front-url">WWW.BRIVOLANEUTE.COM</div>
  </section>

  <section class="card card--back" aria-label="Card back">
    <svg class="swoosh" viewBox="0 0 620 354" width="620" height="354" aria-hidden="true">
      <defs>
        <linearGradient id="glow" x1="0" y1="0" x2="1" y2="1">
          <stop offset="0" stop-color="var(--orange)"/>
          <stop offset="1" stop-color="var(--orange-light)"/>
        </linearGradient>
      </defs>
      <rect width="620" height="354" fill="url(#glow)"/>
      <path d="M300,0 C262,140 330,300 620,318 L620,0 Z" fill="var(--peach)"/>
      <path d="M314,0 C280,138 345,288 620,304 L620,0 Z" fill="var(--red)"/>
      <path d="M330,0 C298,134 362,274 620,288 L620,0 Z" fill="var(--white)"/>
    </svg>

    <div class="identity">
      <h1 class="name">Danielle R Morrow</h1>
      <p class="role">Founder and CEO</p>
    </div>

    <ul class="contacts">
      <li>
        <svg viewBox="0 0 24 24" aria-hidden="true"><path fill="#fff" d="M6.6 10.8a15 15 0 0 0 6.6 6.6l2.2-2.2c.3-.3.7-.4 1-.2 1.1.4 2.3.6 3.6.6.6 0 1 .4 1 1V20c0 .6-.4 1-1 1A17 17 0 0 1 3 4c0-.6.4-1 1-1h3.5c.6 0 1 .4 1 1 0 1.3.2 2.5.6 3.6.1.3 0 .7-.2 1z"/></svg>
        413-926-BRIV
      </li>
      <li>
        <svg viewBox="0 0 24 24" aria-hidden="true"><rect x="2" y="5" width="20" height="14" fill="none" stroke="#fff" stroke-width="2"/><path d="M2 5l10 8 10-8" fill="none" stroke="#fff" stroke-width="2"/></svg>
        dmorrow@brivolaneute.com
      </li>
      <li>
        <svg viewBox="0 0 24 24" aria-hidden="true"><g fill="none" stroke="#fff" stroke-width="1.8"><circle cx="12" cy="12" r="10"/><ellipse cx="12" cy="12" rx="4.5" ry="10"/><path d="M2 12h20M4 7h16M4 17h16"/></g></svg>
        Brivolaneute.com
      </li>
    </ul>

    <p class="division">Brivo Lane Ute is a division of Harmond Vistas. LLC</p>

    <div class="logo">
      <div class="logo-art" role="img" aria-label="Brand illustration area"></div>
      <div class="logo-name">BrivoLane Ute</div>
    </div>
  </section>

</body>
</html>
```